Cultural Values, and Purpose, Vision and Mission statements design

We have recently created Cultural Values, and Purpose, Vision and Mission statements for a client’s business. We would like a visual representation created of each of these, to be hung on display in their office. For this project, we would like four (4) graphic design prints drawn up that depict:1. Purpose2. Vision3. Mission4. Cultural ValuesAll print designs should use a recurring, common theme, and be reflective of the business’ colours (see attached logo.)Please read and follow specifications in attached design brief.
Updates

Need extra days to review

Target Market(s)

Females, aged between 37 and 57 years old, who are family orientated, living locally, married and have between 1 and 3 children living at home.

Requirements
Must have
• Photoshop (PSD) format: All completed design will need to be in Photoshop (PSD) format before being handed over. This is to ensure that we can make alterations before printing if necessary.
• Quality: All designs must be 300 pixels resolution or higher.
• Purpose, Vision & Mission Designs Dimensions: The dimensions for each of the Purpose, Vision and Mission designs will need to be 30.5cm x 40.6cm (portrait, rectangle shape) with a surrounding 3.8cm border as it will be printed onto canvas matching these specifications.
• Cultural Values Dimensions: There are no specific dimensions required for the Cultural Values so the designer should feel free to display them best they see fit.
• Theme: All must follow the same theme and be reflective of the business's colours and logo.

```html
<!DOCTYPE html>
<html lang="en">
<head>
<meta charset="utf-8">
<title>Cultural Values</title>
<link rel="stylesheet" href="https://fonts.googleapis.com/css2?family=Bebas+Neue&family=Montserrat:wght@700&display=swap">
<style>
  :root {
    --paper-light: #f4f4f5;
    --paper-mid: #d6d6d8;
    --paper-edge: #bdbdc0;
    --frame-line: #ffffff;
    --title-band: #939598;
    --title-text: #ffffff;
    --connector: #8a8a8d;
    --pride: #0a67b3;
    --pride-dark: #075497;
    --honesty: #e0004d;
    --honesty-dark: #c20042;
    --respect: #0b9a43;
    --respect-dark: #088437;
    --diligence: #b5860d;
    --diligence-dark: #9c720a;
    --label: #ffffff;
  }
  * { box-sizing: border-box; margin: 0; padding: 0; }
  html, body { width: 1200px; height: 1130px; overflow: hidden; }
  body { background: var(--paper-mid); }
  .values-poster {
    position: relative;
    width: 1200px;
    height: 1130px;
    overflow: hidden;
    background: radial-gradient(ellipse at 50% 48%, var(--paper-light) 0%, var(--paper-mid) 62%, var(--paper-edge) 100%);
  }
  .inner-frame {
    position: absolute;
    left: 44px; top: 50px;
    width: 1114px; height: 1040px;
    border: 3px solid var(--frame-line);
  }
  .title-band {
    position: absolute;
    left: 187px; top: 114px;
    width: 829px; height: 118px;
    background: var(--title-band);
    border-radius: 38px 0 38px 0;
    clip-path: polygon(3% 0, 100% 0, 100% 100%, 0 100%);
    display: flex; align-items: center; justify-content: center;
  }
  .title-band h1 {
    font-family: "Bebas Neue", sans-serif;
    font-weight: 400;
    font-size: 128px;
    line-height: 1;
    color: var(--title-text);
    letter-spacing: 1px;
    padding-top: 10px;
  }
  .connector {
    position: absolute;
    left: 585px; top: 400px;
    width: 9px; height: 560px;
    background: var(--connector);
  }
  .value-pill {
    position: absolute;
    height: 103px;
    display: flex; align-items: center;
    font-family: "Montserrat", sans-serif;
    font-weight: 700;
    font-size: 50px;
    color: var(--label);
    box-shadow: 0 6px 10px rgba(0,0,0,0.18);
  }
  .value-pill--left { border-radius: 12px 0 0 44px; justify-content: center; padding-right: 60px; }
  .value-pill--right { border-radius: 0 12px 44px 0; padding-left: 62px; }
  .value-badge {
    position: absolute;
    width: 127px; height: 127px;
    border-radius: 50%;
    display: flex; align-items: center; justify-content: center;
    box-shadow: 0 6px 10px rgba(0,0,0,0.2);
  }
  .value-badge svg { width: 72px; height: 72px; fill: none; stroke: #fff; stroke-width: 2.6; stroke-linecap: round; stroke-linejoin: round; }

  .pride { background: var(--pride); left: 151px; top: 332px; width: 450px; }
  .pride-badge { background: var(--pride); border: 4px solid var(--pride-dark); left: 527px; top: 320px; }
  .honesty { background: var(--honesty); left: 600px; top: 526px; width: 463px; }
  .honesty-badge { background: var(--honesty); border: 4px solid var(--honesty-dark); left: 529px; top: 514px; }
  .respect { background: var(--respect); left: 146px; top: 720px; width: 460px; }
  .respect-badge { background: var(--respect); border: 4px solid var(--respect-dark); left: 524px; top: 708px; }
  .diligence { background: var(--diligence); left: 600px; top: 914px; width: 460px; }
  .diligence-badge { background: var(--diligence); border: 4px solid var(--diligence-dark); left: 524px; top: 902px; }
  .figure-spot { width: 72px; height: 72px; border-radius: 50%; background: rgba(255,255,255,0.18); }
</style>
</head>
<body>
<main class="values-poster">
  <div class="inner-frame"></div>

  <header class="title-band"><h1>CULTURAL VALUES</h1></header>

  <div class="connector"></div>

  <div class="value-pill value-pill--left pride">PRIDE</div>
  <div class="value-badge pride-badge">
    <div class="figure-spot" role="img" aria-label="Line icon of a strong upper-body figure"></div>
  </div>

  <div class="value-pill value-pill--right honesty">HONESTY</div>
  <div class="value-badge honesty-badge">
    <svg viewBox="0 0 48 48" role="img" aria-label="Heart icon">
      <path d="M24 40 C10 30 5 23 5 16 C5 10 10 6 15 6 C19 6 22 8 24 11 C26 8 29 6 33 6 C38 6 43 10 43 16 C43 23 38 30 24 40 Z"/>
      <path d="M14 24 L20 20 L26 24 L32 20"/>
    </svg>
  </div>

  <div class="value-pill value-pill--left respect">RESPECT</div>
  <div class="value-badge respect-badge">
    <svg viewBox="0 0 48 48" role="img" aria-label="Hands holding a heart icon">
      <path d="M24 26 C18 22 16 19 16 16 C16 13 18 12 20 12 C22 12 23 13 24 15 C25 13 26 12 28 12 C30 12 32 13 32 16 C32 19 30 22 24 26 Z"/>
      <path d="M8 8 L8 24 L16 34 L16 42"/>
      <path d="M40 8 L40 24 L32 34 L32 42"/>
    </svg>
  </div>

  <div class="value-pill value-pill--right diligence">DILIGENCE</div>
  <div class="value-badge diligence-badge">
    <svg viewBox="0 0 48 48" role="img" aria-label="Magnifying glass icon">
      <circle cx="20" cy="20" r="13"/>
      <circle cx="20" cy="20" r="5"/>
      <path d="M30 30 L42 42"/>
    </svg>
  </div>
</main>
</body>
</html>
```